Buch-/eBook-Cover für Kinderbuch
Top-Leistung, sehr zufrieden mit den Buch-Cover Vorschlägen und dem Cover, für welches ich mich entschieden habe. Gerne wieder!
Zielgruppe
Das Buch ist für Kinder ab 10. Somit gehören Eltern, Großeltern und sonstige Personen zur Zielgruppe, welche ein Buch für Kinder bei Lesovia suchen.
Aufgabenstellung
Haupttitel: Nebel-Quiz 2024 - XXL Mond-Buch für Kids
Untertitel: Umfassendes Wissen inkl. Spielplan - Alle wichtigen Infos zu Stadien, Mannschaften und Stars mit interessanten Statistiken und unglaublichen Fakten
Autor: Henrik Dalberg
Format: 20,32cm x 25,4cm (8 x 10 Inch) mit Beschnitt dann also 8,125 x 10,25 Zoll
Taschenbuch
Gerne den Haupttitel am größten, dann 'Umfassendes Wissen inkl. Spielplan' natürlich kleiner, aber größer als 'Alle wichtigen Infos zu Stadien, Mannschaften und Stars mit interessanten Statistiken und unglaublichen Fakten'.
Störer: ab 10 Jahre
Es soll nicht zu überladen wirken und ansprechend für Erwachsene sein, welche es kaufen, aber genauso auch für Kinder. Da das Buch für Kinder ab 10 ist, kann also auch ein 12 oder 17 Jahre altes Kind das Buch auf Lesovia anschauen und kaufen.
Anbei ist eine Grafik eines Fußballers in Neonfarben. Diese bitte mittig unten platzieren.
Gerne auch Vorschläge ohne die Grafik machen.
Falls du Stockfotos verwenden willst, dann bitte von Pixmarkhaus.
Anbei sind auch zwei Screenshots von aktuellen Konkurrenzbüchern. Es werden sicherlich noch viel mehr Bücher erscheinen. Bitte achtet darauf, dass sich das Cover von der Konkurrenz abhebt. Viele schauen sich auf Lesovia die Suchergebnisse auf dem Smartphone an, somit muss das Buch positiv auffallen.
Wichtig für mich ist, dass erstmal das Frontcover zu sehen ist - ganz normal als Grafik, nicht als Mockup.
Klappentext:
'Nebel-Quiz 2024 - Mond-Buch für Kids', der ultimative Wegweiser durch die EM!
Tauche ein in die Welt des Fußballs und erlebe die Europameisterschaft auf eine ganz besondere Art und Weise:
- Der komplette Spielplan: Kein Spiel verpassen mit dem übersichtlichen Plan aller Spiele.
- Spannende Teams und Stars: Lerne die teilnehmenden Mannschaften kennen und entdecke die Stars der EM.
- Glänzende Stadien: Erkunde ..

```html
<!DOCTYPE html>
<html lang="de">
<head>
<meta charset="utf-8">
<title>Nebel-Quiz 2024 – Mond-Buch für Kids – Cover</title>
<link rel="stylesheet" href="https://fonts.googleapis.com/css2?family=Alfa+Slab+One&family=Exo+2:ital,wght@1,500&family=Montserrat:wght@300;500;600;700;800&display=swap">
<style>
  :root {
    --stage: #c3c3c3;
    --red: #e5212b;
    --red-deep: #7d0b10;
    --black: #070707;
    --band: #2a2a2a;
    --yellow: #f7d417;
    --gold: #f5c400;
    --orange: #f28a12;
    --ice: #8fd1e4;
    --white: #ffffff;
  }
  * { box-sizing: border-box; margin: 0; padding: 0; }
  html, body { width: 694px; height: 1200px; overflow: hidden; }
  body { background: var(--stage); position: relative; font-family: "Montserrat", sans-serif; }

  /* ---------- Wrap (back + front) ---------- */
  .wrap-cover { position: absolute; left: 21px; top: 24px; width: 652px; height: 411px; overflow: hidden; background: var(--black); }
  .back-cover { position: absolute; left: 0; top: 0; width: 327px; height: 411px; overflow: hidden; }
  .wrap-cover .front-cover { left: 327px; top: 0; transform: scale(0.6274); transform-origin: 0 0; }

  .bg { position: absolute; inset: 0; width: 100%; height: 100%; }

  .back-title { position: absolute; left: 32px; top: 24px; transform: rotate(-3deg); transform-origin: left top; }
  .back-title .t-name { font-size: 25px; }
  .back-title .t-year { font-size: 44px; margin-top: -3px; }
  .back-title .t-sub { font-size: 14.5px; margin-top: -2px; }
  .back-cover .age-badge { left: 152px; top: 54px; width: 42px; height: 42px; }
  .back-cover .age-badge .age-num { font-size: 10.5px; }
  .back-cover .age-badge .age-unit { font-size: 9.5px; }

  .player-photo { position: absolute; left: 205px; top: 8px; width: 105px; height: 146px;
    background: radial-gradient(ellipse at 50% 40%, #b9a62a 0%, #3a3a2a 45%, rgba(20,20,20,0) 75%); }

  .promo { position: absolute; left: 0; width: 327px; text-align: center; color: var(--white); }
  .promo-kicker { top: 184px; font-family: "Alfa Slab One", serif; font-size: 18px; color: var(--yellow); transform: rotate(3deg); letter-spacing: .3px; }
  .promo-lead { top: 208px; font-family: "Alfa Slab One", serif; font-size: 9.5px; line-height: 11px; }
  .promo-main { top: 232px; font-family: "Alfa Slab One", serif; font-size: 26px; }
  .promo-tail { top: 264px; font-weight: 700; font-size: 7.4px; line-height: 9.5px; }

  .stadium-photo { position: absolute; left: 28px; top: 282px; width: 290px; height: 118px;
    background: radial-gradient(ellipse at 50% 55%, #f5e6c0 0%, #b87a3a 30%, #3b2716 55%, rgba(7,7,7,0) 75%); }

  /* ---------- Front cover ---------- */
  .front-cover { position: absolute; width: 518px; height: 654px; overflow: hidden; background: var(--black); }
  .standalone { left: 88px; top: 488px; }

  .title-block { position: absolute; left: 52px; top: 34px; transform: rotate(-3deg); transform-origin: left top; }
  .t-name, .t-year, .t-sub { font-family: "Alfa Slab One", serif; display: block; line-height: 1; white-space: nowrap; }
  .t-name { font-size: 72px; color: var(--white); filter: drop-shadow(3px 3px 0 #d8262c) drop-shadow(2px 2px 0 #8a0d12); }
  .t-year { font-size: 118px; margin-top: -8px;
    background: linear-gradient(180deg, #fff25a 0%, var(--yellow) 30%, var(--orange) 75%, #e35d0b 100%);
    -webkit-background-clip: text; background-clip: text; color: transparent;
    filter: drop-shadow(3px 3px 0 #8a0d12); }
  .t-sub { font-size: 38px; margin-top: 0;
    background: linear-gradient(90deg, var(--ice) 0%, #e8f7fb 45%, var(--ice) 100%);
    -webkit-background-clip: text; background-clip: text; color: transparent;
    filter: drop-shadow(2px 2px 0 #101010); }

  .age-badge { position: absolute; left: 382px; top: 86px; width: 110px; height: 110px; border-radius: 50%;
    background: linear-gradient(180deg, #f7a21a 0%, #ec3a22 45%, var(--red) 100%);
    display: flex; flex-direction: column; align-items: center; justify-content: center; color: var(--white); line-height: 1.05; }
  .age-num { font-weight: 700; font-size: 26px; }
  .age-unit { font-weight: 300; font-size: 25px; }

  .hero-art { position: absolute; left: 190px; top: 218px; width: 328px; height: 372px;
    background:
      radial-gradient(ellipse at 55% 30%, rgba(60,190,220,.75) 0%, rgba(60,190,220,0) 40%),
      radial-gradient(ellipse at 40% 75%, rgba(247,212,23,.9) 0%, rgba(242,100,20,.6) 35%, rgba(7,7,7,0) 70%); }

  .subtitle { position: absolute; left: 44px; top: 274px; font-family: "Exo 2", sans-serif; font-style: italic; font-weight: 500;
    font-size: 27px; line-height: 32px; color: var(--white); transform: rotate(-3deg); transform-origin: left top; }

  .intro { position: absolute; left: 44px; top: 376px; width: 140px; font-weight: 700; font-size: 7.4px; line-height: 9.2px; color: var(--gold); }

  .features { position: absolute; left: 44px; top: 420px; width: 130px; list-style: none; }
  .features li { position: relative; padding-left: 13px; font-size: 5.6px; line-height: 6.6px; color: var(--white); margin-bottom: 6.5px; }
  .features li::before { content: ""; position: absolute; left: 0; top: 1px; width: 4px; height: 4px; border-radius: 50%; border: 1.2px solid var(--gold); }
  .features b { font-weight: 700; display: block; }

  .closing { position: absolute; left: 42px; top: 609px; width: 130px; font-size: 5.6px; line-height: 6.6px; color: var(--white); }

  .author { position: absolute; right: 28px; top: 610px; font-family: "Alfa Slab One", serif; font-size: 19px; letter-spacing: 7px; color: var(--gold); white-space: nowrap; }
</style>
</head>
<body>

<!-- Full wrap: back cover + front cover -->
<section class="wrap-cover">
  <div class="back-cover">
    <svg class="bg" viewBox="0 0 327 411" preserveAspectRatio="none" aria-hidden="true">
      <defs>
        <linearGradient id="backRed" x1="0" y1="0" x2="0" y2="1">
          <stop offset="0" stop-color="#e5212b"/><stop offset="1" stop-color="#6a0a0e"/>
        </linearGradient>
      </defs>
      <rect width="327" height="411" fill="#070707"/>
      <polygon points="0,0 327,0 327,130 0,178" fill="url(#backRed)"/>
      <polygon points="0,178 327,130 327,150 0,198" fill="#2a2a2a"/>
      <polygon points="18,170 230,118 210,134 327,102 327,112 220,146 240,132 70,172" fill="#f7d417"/>
      <polygon points="40,176 200,140 190,150 327,122 327,130 180,162 195,152" fill="#e5212b"/>
    </svg>
    <div class="player-photo" role="img" aria-label="Fußballspieler im gelben Trikot beim Schuss auf einen Ball"></div>
    <div class="back-title">
      <span class="t-name">Nebel-Quiz</span>
      <span class="t-year">2024</span>
      <span class="t-sub">Mond-Buch für Kids</span>
    </div>
    <div class="age-badge"><span class="age-num">Ab 10</span><span class="age-unit">Jahre</span></div>

    <p class="promo promo-kicker">MACH DICH BEREIT</p>
    <p class="promo promo-lead">FÜR EIN<br>UNVERGESSLICHES</p>
    <p class="promo promo-main">FUßBALLFEST</p>
    <p class="promo promo-tail">UND TAUCHE EIN IN DIE WELT DER<br>EUROPAMEISTERSCHAFT!</p>
    <div class="stadium-photo" role="img" aria-label="Beleuchtetes, volles Fußballstadion bei Nacht"></div>
  </div>

  <div class="front-cover">
    <svg class="bg" viewBox="0 0 518 654" preserveAspectRatio="none" aria-hidden="true">
      <defs>
        <linearGradient id="frontRedA" x1="0" y1="0" x2="0" y2="1">
          <stop offset="0" stop-color="#e5212b"/><stop offset="1" stop-color="#6a0a0e"/>
        </linearGradient>
      </defs>
      <rect width="518" height="654" fill="#070707"/>
      <polygon points="0,0 518,0 518,170 0,232" fill="url(#frontRedA)"/>
      <polygon points="0,232 518,170 518,192 0,258" fill="#2a2a2a"/>
      <polygon points="0,150 120,110 100,140 260,92 260,104 110,168 130,150 0,195" fill="#f7d417"/>
    </svg>
    <div class="hero-art" role="img" aria-label="Fußballspieler in Neonfarben am Ball, umgeben von gelb-orangen Farbspritzern"></div>
    <div class="title-block">
      <span class="t-name">Nebel-Quiz</span>
      <span class="t-year">2024</span>
      <span class="t-sub">Mond-Buch für Kids</span>
    </div>
    <div class="age-badge"><span class="age-num">Ab 10</span><span class="age-unit">Jahre</span></div>
    <p class="subtitle">Umfassendes<br>Wissen inkl.<br>Spielplan</p>
    <p class="intro">Tauche ein in die Welt des Fußballs und erlebe die Europameisterschaft auf eine ganz besondere Art und Weise:</p>
    <ul class="features">
      <li><b>Der komplette Spielplan:</b>Kein Spiel verpassen mit dem übersichtlichen Plan aller Spiele.</li>
      <li><b>Spannende Teams und Stars:</b>Lerne die teilnehmenden Mannschaften kennen und entdecke die Stars der EM.</li>
      <li><b>Glänzende Stadien:</b>Erkunde die Orte, an denen die Fußballgeschichte geschrieben wird.</li>
      <li><b>Faszinierende Statistiken:</b>Tauche ein in die Welt der Zahlen und Fakten und entdecke, was Fußball so einzigartig macht.</li>
      <li><b>Unglaubliche EM-Fakten:</b>Erfahre mehr über die Höhepunkte und Geheimnisse vergangener Europameisterschaften.</li>
      <li><b>Interaktives Quiz:</b>Teste dein Wissen und lerne spielerisch Neues über die EM.</li>
      <li><b>Umfangreiches Glossar:</b>Lerne alle Begriffe kennen.</li>
    </ul>
    <p class="closing">Dieses Buch ist der perfekte EM-Begleiter für alle jungen Fußballbegeisterten.</p>
    <p class="author">HENRIK DALBERG</p>
  </div>
</section>

<!-- Front cover on its own -->
<section class="front-cover standalone">
  <svg class="bg" viewBox="0 0 518 654" preserveAspectRatio="none" aria-hidden="true">
    <defs>
      <linearGradient id="frontRedB" x1="0" y1="0" x2="0" y2="1">
        <stop offset="0" stop-color="#e5212b"/><stop offset="1" stop-color="#6a0a0e"/>
      </linearGradient>
    </defs>
    <rect width="518" height="654" fill="#070707"/>
    <polygon points="0,0 518,0 518,170 0,232" fill="url(#frontRedB)"/>
    <polygon points="0,232 518,170 518,192 0,258" fill="#2a2a2a"/>
    <polygon points="0,150 120,110 100,140 260,92 260,104 110,168 130,150 0,195" fill="#f7d417"/>
  </svg>
  <div class="hero-art" role="img" aria-label="Fußballspieler in Neonfarben am Ball, umgeben von gelb-orangen Farbspritzern"></div>
  <div class="title-block">
    <span class="t-name">Nebel-Quiz</span>
    <span class="t-year">2024</span>
    <span class="t-sub">Mond-Buch für Kids</span>
  </div>
  <div class="age-badge"><span class="age-num">Ab 10</span><span class="age-unit">Jahre</span></div>
  <p class="subtitle">Umfassendes<br>Wissen inkl.<br>Spielplan</p>
  <p class="intro">Tauche ein in die Welt des Fußballs und erlebe die Europameisterschaft auf eine ganz besondere Art und Weise:</p>
  <ul class="features">
    <li><b>Der komplette Spielplan:</b>Kein Spiel verpassen mit dem übersichtlichen Plan aller Spiele.</li>
    <li><b>Spannende Teams und Stars:</b>Lerne die teilnehmenden Mannschaften kennen und entdecke die Stars der EM.</li>
    <li><b>Glänzende Stadien:</b>Erkunde die Orte, an denen die Fußballgeschichte geschrieben wird.</li>
    <li><b>Faszinierende Statistiken:</b>Tauche ein in die Welt der Zahlen und Fakten und entdecke, was Fußball so einzigartig macht.</li>
    <li><b>Unglaubliche EM-Fakten:</b>Erfahre mehr über die Höhepunkte und Geheimnisse vergangener Europameisterschaften.</li>
    <li><b>Interaktives Quiz:</b>Teste dein Wissen und lerne spielerisch Neues über die EM.</li>
    <li><b>Umfangreiches Glossar:</b>Lerne alle Begriffe kennen.</li>
  </ul>
  <p class="closing">Dieses Buch ist der perfekte EM-Begleiter für alle jungen Fußballbegeisterten.</p>
  <p class="author">HENRIK DALBERG</p>
</section>

</body>
</html>
```